Professional Photography Business cards

I need business cards that include my logo which I have uploaded. I run a photography business. I am open to ideas but I would like one side to have my logo and the other side to have my contact info. I don't have a website made but I do own a website domain. I have uploaded 2 different logo color schemes. My business colors are Blue, black , and white.

Business Name
Business Phone Number
Business Email
Business Website address
Instagram

Industry/Entity Type

Professional Photography

Contact Information for Business Card

Phone Number: 555-314-8027 email: info@tkellan-studios.example Instagram: @t.kellanstudios website doman- www.tkellan-studios.example

Requirements
Must have
• I like the idea of a business card with a full black background front and back of card. My colors must include royal blue, black, and white

```html
<!DOCTYPE html>
<html lang="en">
<head>
<meta charset="utf-8">
<title>T. Kellan Studios — Business Card</title>
<link href="https://fonts.googleapis.com/css2?family=Open+Sans:wght@400;600&display=swap" rel="stylesheet">
<style>
  :root {
    --page-bg: #1a1a1b;
    --card-black: #141415;
    --card-edge: #222224;
    --text-white: #f2f2f2;
    --royal-blue: #3a3fc4;
    --icon-blue: #3d44b8;
    --silver: #8d8d90;
  }
  * { box-sizing: border-box; margin: 0; padding: 0; }
  html, body {
    width: 1200px; height: 900px; overflow: hidden;
    background: var(--page-bg);
    font-family: "Open Sans", Arial, sans-serif;
  }
  .sheet {
    width: 1200px; height: 900px;
    display: flex; flex-direction: column;
    align-items: center; justify-content: center; gap: 56px;
  }
  .card {
    width: 660px; height: 378px;
    background: var(--card-black);
    border: 1px solid var(--card-edge);
    border-radius: 22px;
    box-shadow: 0 18px 40px rgba(0,0,0,.55);
    position: relative;
  }
  .card--contact { display: flex; align-items: center; padding: 0 48px; }
  .contact-list { list-style: none; flex: 1; }
  .contact-list li {
    display: flex; align-items: center; gap: 10px;
    color: var(--text-white); font-size: 17px; line-height: 1.6;
  }
  .contact-icon { width: 14px; height: 14px; flex: none; }
  .brand {
    display: flex; align-items: center; gap: 14px;
  }
  .brand-mark {
    width: 52px; height: 52px; border-radius: 50%;
    border: 3px solid var(--text-white); flex: none;
  }
  .brand-name {
    font-size: 28px; font-weight: 600; color: var(--royal-blue);
    white-space: nowrap;
  }
  .card--logo { display: flex; align-items: center; justify-content: center; }
  .card--logo .brand-name { color: var(--silver); font-size: 40px; }
  .card--logo .brand-mark { border-color: var(--silver); width: 74px; height: 74px; }
</style>
</head>
<body>
<main class="sheet">
  <section class="card card--contact" aria-label="Contact side">
    <ul class="contact-list">
      <li>
        <svg class="contact-icon" viewBox="0 0 16 16" aria-hidden="true"><path fill="var(--icon-blue)" d="M3.5 1.5l2.5 0 1 3.5-1.8 1.2a9 9 0 0 0 4.6 4.6L11 9l3.5 1v2.5c0 1-1 2-2 2A11 11 0 0 1 1.5 3.5c0-1 1-2 2-2z"/></svg>
        555-314-8027
      </li>
      <li>
        <svg class="contact-icon" viewBox="0 0 16 16" aria-hidden="true"><rect x="1" y="3" width="14" height="10" rx="1" fill="var(--icon-blue)"/><path d="M1.5 3.5 8 9l6.5-5.5" stroke="var(--card-black)" stroke-width="1.3" fill="none"/></svg>
        info@tkellan-studios.example
      </li>
      <li>
        <svg class="contact-icon" viewBox="0 0 16 16" aria-hidden="true"><circle cx="8" cy="8" r="7" fill="var(--icon-blue)"/><path d="M1 8h14M8 1c-3 3.5-3 10.5 0 14M8 1c3 3.5 3 10.5 0 14" stroke="var(--card-black)" stroke-width="1.1" fill="none"/></svg>
        www.tkellan-studios.example
      </li>
      <li>
        <svg class="contact-icon" viewBox="0 0 16 16" aria-hidden="true"><circle cx="8" cy="8" r="6.5" fill="none" stroke="var(--icon-blue)" stroke-width="1.8"/></svg>
        @t.kellanstudios
      </li>
    </ul>
    <div class="brand">
      <span class="brand-name">T. Kellan Studios</span>
      <span class="brand-mark" aria-hidden="true"></span>
    </div>
  </section>

  <section class="card card--logo" aria-label="Logo side">
    <div class="brand">
      <span class="brand-name">T. Kellan Studios</span>
      <span class="brand-mark" aria-hidden="true"></span>
    </div>
  </section>
</main>
</body>
</html>
```